Lumen Table

A quick run down of the iPhone app and what it does:

1. It has a home screen for that restaurant that will guide you to the menu.
2. You can search the menu which has all the pictures of the items on the menu.
3. There are also ratings from the users on each item.
4. You can also order and pay from the app.

Please see this link to look at the wire-frame we have created (Click on the buttons to move from page to page)
https://www.wireplank.com/editor/live/preview/p_3KdLmwqZxPtrbvHjsNcYeRu7TAgkpo2x.5520918374612

We would like something that is very clean, minimalist and uses modern design to convey the feeling of cultured.

I would like the designer to create at least 5 pages:

1. The Home screen to the restaurant. (call it Harbor Plate) You can redo the buttons to make it look better. Like have a logo or something better than box buttons. Please use good looking easy to read fonts, Modern you might say.

2. and 3. The Menu page with 3 items and pictures per menu title like Appetizers and Entrees have it look as if it is dropping down (you can use your own photos or some from the web with descriptions like what you see on the Wire-frame)

4. The item drill down, as you click on an item from the menu it comes up with a larger photo of the item and the description and also the rating under the description. (see wire-frame)

5. The order page with items from the menu on the order page with prices.

I would like for the bottom menu to be updated with some nice looking buttons. For one the help now button I would like to have a circle with an outline of a person raising their hand.

I currently don't have a logo or photos so I will rely on your discretion to find the photos you need. I also have no particular colors in mind but here are some app designs I really like.

http://gallopix-gallery.com/tagged/app_vemo#show-all

http://31.media.pinvalecdn.com/3f8a1c9e2b7d40a6e5c8f1b2d9a47e60/pinvale_k4rtbqwzXP2m83hy1_400.png (put the item name on this and a plus sign in the top right of the photo)

http://37.media.pinvalecdn.com/a92e7b0c4f6d18e3b5a0c7d2e8f14b93/pinvale_k4rtb2xqLM5m83hy1_400.png ( take out all the words and put in all the information I have on the page with the large picture, from my wire-frame, the drill down page)

If you follow the same sort of app design with a photo in the background of the restaurant home page and clear design like this you will for sure win.

Also after this is done I will most likely have the winning designer create my logo, and app icon.

Target Market(s)

The target market of this App are people that can afford to eat out and enjoy using technology to have a better dining experience. Ages 16 to 45 Male and Female.

Industry/Entity Type

Restaurant

Font styles to use
Sans Serif

Requirements
Must have
• Clear, high quality photos, I don't want to see any individual pixels. Please read my outline carefully to understand what this app will do.
Nice to have
• I want to feel like I'm having a good experience from the moment I open the app the the moment I finish my meal with the app. Come up with something simple and creative for the user to experience while dining.
Should not have
• Please do not just submit my wire-frame in different colors that will be a waste of your time and mine. I don't want to see boxes as the buttons.

```html
<!DOCTYPE html>
<html lang="en">
<head>
<meta charset="utf-8">
<title>Lumen Table – Harbor Plate app screens</title>
<link href="https://fonts.googleapis.com/css2?family=Oswald:wght@400;500;600&family=Open+Sans:wght@400;600;700&display=swap" rel="stylesheet">
<style>
:root{
  --page:#ececec;
  --screen:#141414;
  --panel:#1c1c1c;
  --bar:#0d0d0d;
  --text:#ffffff;
  --muted:#a8a8a8;
  --star:#4a8fd0;
  --accent:#4a7aa6;
  --chip:rgba(40,28,22,.78);
}
*{box-sizing:border-box;margin:0;padding:0}
html,body{width:1200px;height:576px;overflow:hidden;background:var(--page)}
body{font-family:"Open Sans",Arial,sans-serif;color:var(--text);position:relative}
.screen{position:absolute;top:95px;width:220px;height:386px;background:var(--screen);overflow:hidden}
.s1{left:12px}.s2{left:249px}.s3{left:490px}.s4{left:731px}.s5{left:968px}
.status{position:absolute;top:0;left:0;right:0;height:14px;background:#000;font-size:7px;font-weight:600;display:flex;justify-content:space-between;align-items:center;padding:0 5px;z-index:5}
.tabbar{position:absolute;bottom:0;left:0;right:0;height:34px;background:var(--bar);display:flex;justify-content:space-around;align-items:center;z-index:5}
.tab{display:flex;flex-direction:column;align-items:center;gap:1px;font-family:"Oswald",sans-serif;font-size:4.5px;letter-spacing:.2px;text-transform:uppercase}
.tab-icon{width:20px;height:20px;border:1.3px solid #fff;border-radius:50%;display:flex;align-items:center;justify-content:center}
.tab-icon svg{width:11px;height:11px;fill:none;stroke:#fff;stroke-width:1.4;stroke-linecap:round}
.tabbar.wide .tab-icon{width:24px;height:24px}
.tabbar.wide .tab{font-size:5px}
.photo{position:absolute;left:0;right:0}
.bg-warm{top:14px;bottom:34px;background:radial-gradient(circle at 70% 45%,#c9772f 0%,#7a4220 25%,#3c2418 55%,#1a120e 90%)}
.brand{position:absolute;left:38px;top:170px;display:flex;align-items:center;gap:6px}
.brand-dot{width:22px;height:22px;border-radius:50%;background:#fff}
.brand-name{font-family:"Oswald",sans-serif;font-weight:500;font-size:13px;line-height:13px;text-transform:uppercase;color:#fff}
.search{position:absolute;top:22px;left:10px;right:10px;height:12px;border-radius:6px;background:rgba(255,255,255,.25)}
.search::after{content:"";position:absolute;left:4px;top:2px;width:6px;height:6px;border:1px solid #fff;border-radius:50%}
.cat{position:absolute;width:76px;height:76px;border-radius:50%;background:var(--chip);display:flex;flex-direction:column;align-items:center;justify-content:center;gap:5px;font-family:"Oswald",sans-serif;font-size:6.5px;text-transform:uppercase}
.cat svg{width:26px;height:26px;fill:#fff}
.pager{position:absolute;top:306px;left:0;right:0;display:flex;justify-content:center;align-items:center;gap:12px}
.pager span{width:10px;height:10px;border-radius:50%;background:rgba(255,255,255,.35)}
.pager .on{width:24px;height:24px;background:var(--accent)}
.navbar{position:absolute;top:14px;left:0;right:0;height:15px;background:#000;font-size:7px;text-align:center;line-height:15px}
.navbar .back{position:absolute;left:5px}
.item{position:absolute;left:0;right:0;height:155px}
.item-photo{position:absolute;inset:0 0 40px 0}
.food-a{background:radial-gradient(circle at 35% 65%,#b8202a 0%,#5f8a3e 30%,#3b4a40 60%,#20292a 100%)}
.food-b{background:radial-gradient(circle at 50% 50%,#e0343c 0%,#b41c25 45%,#6a1518 80%,#2f1113 100%)}
.item-info{position:absolute;left:0;right:0;bottom:0;height:40px;background:var(--panel);padding:4px 6px}
.item-name{font-size:11px;display:flex;justify-content:space-between}
.item-name b{font-weight:700}
.rate{font-size:5.5px;color:var(--muted);display:flex;align-items:center;gap:3px}
.stars{color:var(--star);font-size:9px;letter-spacing:.5px}
.stars i{color:#fff;font-style:normal}
.plus{position:absolute;top:8px;right:6px;width:17px;height:17px;border:1.3px solid #fff;border-radius:50%;font-size:13px;line-height:13px;text-align:center}
.detail-photo{top:14px;height:108px;background:radial-gradient(circle at 35% 70%,#b8202a 0%,#5f8a3e 30%,#404d44 60%,#1e2626 100%)}
.detail-head{position:absolute;top:106px;left:10px;right:8px;display:flex;justify-content:space-between;align-items:center;font-size:10px}
.desc{position:absolute;top:122px;left:8px;right:8px;font-size:6px;line-height:8px;color:#ddd}
.reviews-head{position:absolute;top:148px;left:0;right:0;text-align:center;font-size:6.5px;font-weight:700}
.count{position:absolute;right:10px;top:-4px;width:15px;height:15px;border:1px solid var(--star);border-radius:50%;color:var(--star);font-size:6px;line-height:13px}
.review{position:absolute;left:8px;right:8px;font-size:6px;line-height:7.5px;text-align:center;color:#ddd}
.review .who{display:flex;justify-content:space-between;text-align:left;font-weight:700;color:#fff;margin-bottom:3px}
.review .who span{font-weight:400;font-size:5.5px;display:flex;align-items:center;gap:2px}
.review q{display:block;font-weight:700;color:#fff}
.order-row{position:absolute;left:10px;right:10px;display:flex;justify-content:space-between;align-items:flex-start;font-weight:700;font-size:10px}
.qty{display:flex;align-items:center;gap:4px;font-weight:400}
.qty .btn{width:13px;height:13px;border:1px solid #fff;border-radius:50%;font-size:10px;line-height:11px;text-align:center}
.qty .num{width:13px;text-align:center;font-size:7px;background:#2a2a2a;line-height:10px;position:relative}
.qty .num small{position:absolute;top:11px;left:0;right:0;font-size:5px;color:var(--muted)}
.subtotal{position:absolute;top:170px;right:30px;font-weight:700;font-size:10px;display:flex;gap:14px}
.submit{position:absolute;top:298px;left:22px;width:155px;height:25px;border-radius:2px;background:var(--accent);font-size:8px;font-weight:600;text-align:center;line-height:25px}
</style>
</head>
<body>

<!-- Home -->
<section class="screen s1">
  <div class="status"><span>●●●○○ NOVA</span><span>4:21 PM</span><span>22%</span></div>
  <div class="photo bg-warm" role="img" aria-label="Blurred warm-lit restaurant interior"></div>
  <div class="brand"><span class="brand-dot"></span><span class="brand-name">Lumen Table<br>Harbor Plate</span></div>
  <nav class="tabbar">
    <div class="tab"><span class="tab-icon"><svg viewBox="0 0 12 12"><path d="M2 8h8M3 8a3 3 0 0 1 6 0"/></svg></span>Order</div>
    <div class="tab"><span class="tab-icon"><svg viewBox="0 0 12 12"><path d="M4 4a2 2 0 1 1 2 2v1.5M6 9.5v.1"/></svg></span>Help Now</div>
    <div class="tab"><span class="tab-icon"><svg viewBox="0 0 12 12"><path d="M3 2v8M9 2v8M2 2v3h2V2"/></svg></span># Table</div>
    <div class="tab"><span class="tab-icon"><svg viewBox="0 0 12 12"><path d="M3 3.5h6M3 6h6M3 8.5h6"/></svg></span>Menu</div>
  </nav>
</section>

<!-- Menu categories -->
<section class="screen s2">
  <div class="status"><span>●●●○○ NOVA</span><span>4:21 PM</span><span>22%</span></div>
  <div class="photo bg-warm" role="img" aria-label="Blurred warm-lit restaurant interior"></div>
  <div class="search"></div>
  <div class="cat" style="left:12px;top:42px"><svg viewBox="0 0 24 24"><path d="M6 6h12l-2 16H8z"/></svg>Drinks</div>
  <div class="cat" style="left:122px;top:42px"><svg viewBox="0 0 24 24"><path d="M3 21L21 3l1 1L4 22z"/><circle cx="9" cy="15" r="3"/><circle cx="14" cy="10" r="3"/></svg>Appetizers</div>
  <div class="cat" style="left:12px;top:128px"><svg viewBox="0 0 24 24"><path d="M4 11a8 6 0 0 1 16 0zM4 13h16v2H4zM4 17h16a3 3 0 0 1-3 3H7a3 3 0 0 1-3-3z"/></svg>Entrees</div>
  <div class="cat" style="left:122px;top:128px"><svg viewBox="0 0 24 24"><circle cx="12" cy="7" r="4"/><path d="M5 22v-6a7 5 0 0 1 14 0v6z"/></svg>Chef's Choice</div>
  <div class="cat" style="left:12px;top:214px"><svg viewBox="0 0 24 24"><path d="M3 12h18v9H3zM6 8h12v3H6z"/></svg>Desserts</div>
  <div class="cat" style="left:122px;top:214px"><svg viewBox="0 0 24 24"><circle cx="5" cy="12" r="2.5"/><circle cx="12" cy="12" r="2.5"/><circle cx="19" cy="12" r="2.5"/></svg>Others</div>
  <div class="pager"><span></span><span class="on"></span><span></span></div>
  <nav class="tabbar">
    <div class="tab"><span class="tab-icon"><svg viewBox="0 0 12 12"><path d="M2 8h8M3 8a3 3 0 0 1 6 0"/></svg></span>Order</div>
    <div class="tab"><span class="tab-icon"><svg viewBox="0 0 12 12"><path d="M4 4a2 2 0 1 1 2 2v1.5M6 9.5v.1"/></svg></span>Help Now</div>
    <div class="tab"><span class="tab-icon"><svg viewBox="0 0 12 12"><path d="M3 2v8M9 2v8M2 2v3h2V2"/></svg></span># Table</div>
    <div class="tab"><span class="tab-icon"><svg viewBox="0 0 12 12"><path d="M3 3.5h6M3 6h6M3 8.5h6"/></svg></span>Menu</div>
  </nav>
</section>

<!-- Appetizers list -->
<section class="screen s3">
  <div class="status"><span>●●●○○ NOVA</span><span>4:21 PM</span><span>22%</span></div>
  <div class="navbar"><span class="back">&lt; Back</span>Appetizers</div>
  <article class="item" style="top:29px">
    <div class="item-photo food-a" role="img" aria-label="Cucumber cups topped with tomato beside vegetable sticks in glasses"></div>
    <span class="plus">+</span>
    <div class="item-info"><div class="item-name"><span>Cucumber Cup</span><b>$10</b></div><div class="rate">Rating <span class="stars">★★★★</span></div></div>
  </article>
  <article class="item" style="top:186px">
    <div class="item-photo food-b" role="img" aria-label="Watermelon cubes topped with whipped cheese on a platter"></div>
    <span class="plus">+</span>
    <div class="item-info"><div class="item-name"><span>Watermelon Cup</span><b>$8</b></div><div class="rate">Rating <span class="stars">★★★</span></div></div>
  </article>
  <nav class="tabbar">
    <div class="tab"><span class="tab-icon"><svg viewBox="0 0 12 12"><path d="M2 8h8M3 8a3 3 0 0 1 6 0"/></svg></span>Order</div>
    <div class="tab"><span class="tab-icon"><svg viewBox="0 0 12 12"><circle cx="6" cy="7" r="1.3"/><path d="M6 8.5v2M6 5.5V2"/></svg></span>Help Now</div>
    <div class="tab"><span class="tab-icon"><svg viewBox="0 0 12 12"><path d="M3 2v8M9 2v8M2 2v3h2V2"/></svg></span># Table</div>
    <div class="tab"><span class="tab-icon"><svg viewBox="0 0 12 12"><path d="M3 3.5h6M3 6h6M3 8.5h6"/></svg></span>Menu</div>
  </nav>
</section>

<!-- Item detail -->
<section class="screen s4">
  <div class="status"><span>●●●○○ NOVA</span><span>4:21 PM</span><span>22%</span></div>
  <div class="photo detail-photo" role="img" aria-label="Cucumber cups with tomato and vegetable sticks in glasses"></div>
  <span class="plus" style="top:18px">+</span>
  <div class="detail-head"><span>Cucumber Cup</span><span class="rate">Rating <span class="stars">★★★★</span></span></div>
  <p class="desc">Refreshing combination of Cucumber and goat cheese in Herbed Goat Cheese-Cucumber Party Bites.</p>
  <div class="reviews-head">Reviews<span class="count">23</span></div>
  <div class="review" style="top:172px">
    <div class="who">Owen Carter<span>Rating <span class="stars">★★★★★</span></span></div>
    <q>Very cool spot with great appetizers!</q>
    We found this place upon recommendation of restaurant close by. We sat at the bar, had a few drinks, some appetizers &amp; enjoyed chatting with the owner. Really enjoyed.
  </div>
  <div class="review" style="top:238px">
    <div class="who">Liam<span>Rating <span class="stars">★★★★<i>★</i></span></span></div>
    <q>Great evening of wine tasting</q>
    Five friends enjoyed a great evening of wine tasting, we also came back rather late the following evening
  </div>
  <div class="review" style="top:290px">
    <div class="who">Noah</div>
    <q>Watermelon cup</q>
  </div>
  <nav class="tabbar wide">
    <div class="tab"><span class="tab-icon"><svg viewBox="0 0 12 12"><circle cx="6" cy="7" r="1.3"/><path d="M6 8.5v2M6 5.5V2"/></svg></span>Help Now</div>
    <div class="tab"><span class="tab-icon"><svg viewBox="0 0 12 12"><path d="M2 8h8M3 8a3 3 0 0 1 6 0"/></svg></span>Order</div>
  </nav>
</section>

<!-- Order -->
<section class="screen s5">
  <div class="status"><span>●●●○○ NOVA</span><span>4:21 PM</span><span>22%</span></div>
  <div class="order-row" style="top:28px"><span>Cucumber Cup</span><span class="qty"><span class="btn">+</span><span class="num">2<small>$10</small></span><span class="btn">−</span></span></div>
  <div class="order-row" style="top:66px"><span>Root Fizz</span><span class="qty"><span class="btn">+</span><span class="num">2<small>$5</small></span><span class="btn">−</span></span></div>
  <div class="order-row" style="top:102px"><span>Lemon Spark</span><span class="qty"><span class="btn">+</span><span class="num">1<small>$3</small></span><span class="btn">−</span></span></div>
  <div class="order-row" style="top:136px"><span>Cheese Burger</span><span class="qty"><span class="btn">+</span><span class="num">1<small>$5</small></span><span class="btn">−</span></span></div>
  <div class="subtotal"><span>Sub Total</span><span>$38</span></div>
  <div class="submit">Submit Order</div>
  <nav class="tabbar wide">
    <div class="tab"><span class="tab-icon"><svg viewBox="0 0 12 12"><path d="M3 9l6-6"/></svg></span>Review</div>
    <div class="tab"><span class="tab-icon"><svg viewBox="0 0 12 12"><circle cx="6" cy="4" r="1.5"/><path d="M3 10a3 3 0 0 1 6 0"/></svg></span>Note for Waiter</div>
    <div class="tab"><span class="tab-icon"><svg viewBox="0 0 12 12"><path d="M8 3.5H5a1.2 1.2 0 0 0 0 2.5h2a1.2 1.2 0 0 1 0 2.5H4M6 2v8"/></svg></span>Pay Now</div>
  </nav>
</section>

</body>
</html>
```